Compnay PowerPoint Tempalte Design

I am needing a good base design and slide designs for interior and exterior company presentations. The template will need to be on the company brand with proper coloring and fonts. Able to be creative with layout options with a good example attached.
website for reference: www.crewvantor.com/

Target Market(s)

Professionals

Font styles to use
Other font styles liked:
• Helvetica

Requirements
Must have
• On Brand Colors, Clean, simple design

```html
<!DOCTYPE html>
<html lang="en">
<head>
<meta charset="utf-8">
<title>Crewvantor Presentation Template</title>
<link rel="stylesheet" href="https://fonts.googleapis.com/css2?family=Arimo:wght@400;700&display=swap">
<style>
:root{
  --teal:#1f9c98;
  --teal-dark:#167673;
  --teal-soft:#8fd0cc;
  --navy:#1c2833;
  --navy-mid:#2c3e4c;
  --ink:#3a4650;
  --grey:#8a949c;
  --rule:#d9e0e3;
  --light:#eef3f4;
  --white:#ffffff;
  --page:#f1f3f4;
}
*{box-sizing:border-box}
html,body{margin:0;padding:0}
body{width:1200px;height:3124px;overflow:hidden;background:var(--page);font-family:'Arimo',Arial,Helvetica,sans-serif;color:var(--ink);position:relative}
p,h1,h2,h3,ul{margin:0;padding:0}
.slide{position:absolute;width:560px;height:316px;background:var(--white);overflow:hidden;box-shadow:0 1px 4px rgba(0,0,0,.14)}
.slide > *{position:absolute}
.hero{left:220px;top:165px;transform:scale(1.3571);transform-origin:top left;box-shadow:0 2px 10px rgba(0,0,0,.18)}
.foot{left:0;right:0;bottom:0;height:12px;background:var(--teal);color:var(--white);font-size:5px;line-height:12px;text-align:center;letter-spacing:.3px}
.brand{display:flex;align-items:center;gap:4px;font-weight:700;font-size:11px;color:var(--navy);letter-spacing:.4px}
.brand-mark{width:9px;height:9px;background:var(--teal)}
.slide-title{font-size:17px;font-weight:400;color:var(--navy);text-align:center;left:0;right:0}
.title-mark{left:274px;width:12px;height:8px;background:var(--teal)}
.body-copy{font-size:6px;line-height:1.45;color:var(--grey)}
.photo{background:linear-gradient(135deg,#6aa9a8,#3d8a8c 55%,#2d6470)}
.photo-city{background:linear-gradient(160deg,#4f6e80,#2b4454 50%,#1a2a35)}

/* Title slides */
.site-url{left:20px;top:14px;font-size:7px;color:var(--teal)}
.title-photo{left:0;top:62px;width:100%;height:160px}
.title-overlay{left:0;top:62px;width:64%;height:160px;background:linear-gradient(90deg,rgba(31,156,152,.96),rgba(31,156,152,.75) 65%,rgba(31,156,152,0))}
.title-brand{right:22px;top:26px}
.title-main{left:22px;top:78px;color:var(--white);font-size:23px;font-weight:400;line-height:1.05}
.title-kicker{display:block;font-size:28px;font-weight:700}
.title-sub{left:0;top:150px;width:64%;background:rgba(255,255,255,.88);color:var(--navy);font-size:11px;padding:5px 22px}
.title-date{left:22px;top:234px;font-size:7px;color:var(--grey)}
.dark{background:var(--navy)}
.dark .site-url{color:var(--grey)}
.dark .brand{color:var(--white)}
.dark .title-overlay{background:linear-gradient(90deg,rgba(28,40,51,.97),rgba(28,40,51,.75) 65%,rgba(28,40,51,0))}
.dark .title-date{color:#c5ccd1}

/* Table of contents */
.toc-list{left:60px;top:70px;width:440px;display:grid;grid-template-columns:1fr 1fr;gap:22px 40px;list-style:none}
.toc-item{display:flex;gap:10px;align-items:flex-start}
.toc-num{font-size:18px;color:var(--teal);font-weight:700;line-height:1}
.toc-head{font-size:8px;font-weight:700;color:var(--teal);margin-bottom:3px}

/* About */
.about-title{left:30px;top:30px;font-size:18px;color:var(--navy)}
.about-rule{left:30px;top:56px;width:30px;height:3px;background:var(--teal)}
.about-copy{left:30px;top:70px;width:210px}
.about-frame{left:270px;top:58px;width:262px;height:160px;border:3px solid var(--teal)}
.about-photo{left:260px;top:48px;width:262px;height:160px}

/* Two photos */
.duo-photo{top:22px;width:220px;height:110px;border-bottom:4px solid var(--teal)}
.duo-head{top:150px;font-size:12px;font-weight:700;color:var(--navy)}
.duo-copy{top:170px;width:220px}

/* Team */
.team-band{left:0;top:0;width:100%;height:80px}
.team-band-tint{left:0;top:0;width:100%;height:80px;background:rgba(31,156,152,.7)}
.team-title{left:0;right:0;top:24px;text-align:center;color:var(--white);font-size:17px}
.member{top:96px;width:140px;text-align:center}
.member-photo{width:62px;height:62px;border-radius:50%;border:3px solid var(--teal);margin:0 auto 8px;background:linear-gradient(160deg,#c9b8a8,#8e7d70)}
.member-name{font-size:7px;font-weight:700;color:var(--teal)}
.member-role{font-size:6px;color:var(--grey);margin:2px 0 5px}

/* Values */
.values-band{left:0;top:0;width:100%;height:140px}
.values-tint{left:0;top:0;width:100%;height:140px;background:rgba(31,156,152,.82)}
.values-title{left:0;right:0;top:26px;text-align:center;color:var(--white);font-size:17px}
.values-intro{left:90px;top:56px;width:380px;text-align:center;color:#e6f4f3}
.values-row{left:30px;top:126px;width:500px;display:grid;grid-template-columns:repeat(4,1fr);gap:16px}
.value-icon{width:30px;height:30px;border-radius:50%;background:var(--teal);border:3px solid var(--white);margin:0 auto 8px}
.value-name{font-size:7px;font-weight:700;color:var(--navy);text-align:center;margin-bottom:4px}
.values-row .body-copy{text-align:center}

/* Pyramid */
.pyr-svg{left:170px;top:90px}
.pyr-note{width:120px}
.pyr-note h3{font-size:8px;color:var(--teal);margin-bottom:3px}

/* Process */
.process-line{left:60px;top:119px;width:440px;height:2px;background:var(--rule)}
.step{top:100px;width:100px;text-align:center}
.step-num{width:40px;height:40px;border-radius:50%;background:var(--teal);color:var(--white);font-size:16px;font-weight:700;line-height:40px;margin:0 auto 12px;box-shadow:0 0 0 4px #d8efee}
.step-head{font-size:8px;font-weight:700;color:var(--teal);margin-bottom:4px}

/* Table */
.data-table{left:30px;top:66px;width:500px;border-collapse:collapse;font-size:6.5px}
.data-table th{background:var(--teal);color:var(--white);font-weight:700;padding:5px 6px;text-align:center}
.data-table th:first-child,.data-table td:first-child{text-align:left}
.data-table td{padding:5px 6px;color:var(--ink);text-align:center;border-bottom:1px solid var(--rule)}
.data-table tr:nth-child(even) td{background:var(--light)}

/* Chart */
.chart-svg{left:24px;top:60px}
.chart-table{left:330px;top:74px;width:206px;border-collapse:collapse;font-size:6px}
.chart-table th{background:var(--navy);color:var(--white);padding:4px;text-align:center}
.chart-table td{padding:4px;border-bottom:1px solid var(--rule);text-align:center}
.chart-table td:first-child,.chart-table th:first-child{text-align:left}

/* Contact */
.contact-bg{left:0;top:0;width:100%;height:100%}
.contact-tint{left:0;top:0;width:100%;height:100%;background:linear-gradient(90deg,rgba(28,40,51,.94),rgba(28,40,51,.55))}
.contact-brand{left:36px;top:84px;font-size:15px}
.contact-head{left:36px;top:124px;color:var(--white);font-size:14px}
.contact-list{left:36px;top:150px;list-style:none;color:#d7dde1;font-size:7px}
.contact-list li{display:flex;align-items:center;gap:7px;margin-bottom:7px}
.contact-icon{width:14px;height:14px;border-radius:50%;background:var(--teal);display:flex;align-items:center;justify-content:center}
</style>
</head>
<body>

<!-- Hero title slide -->
<section class="slide title-slide hero">
  <p class="site-url">www.crewvantor.com/</p>
  <div class="photo title-photo" role="img" aria-label="Photo of a smiling business team"></div>
  <div class="title-overlay"></div>
  <div class="brand title-brand"><span class="brand-mark"></span>CREWVANTOR</div>
  <h1 class="title-main"><span class="title-kicker">PRESENTATION</span>Title Goes Here!</h1>
  <p class="title-sub">Subtitle of Presentation Goes Here</p>
  <p class="title-date">September 20, 2024</p>
  <footer class="foot">Copyright © 2024 Crewvantor. All rights reserved.</footer>
</section>

<!-- Title light, team photo -->
<section class="slide title-slide" style="left:30px;top:784px">
  <p class="site-url">www.crewvantor.com/</p>
  <div class="photo title-photo" role="img" aria-label="Photo of a smiling business team"></div>
  <div class="title-overlay"></div>
  <div class="brand title-brand"><span class="brand-mark"></span>CREWVANTOR</div>
  <h1 class="title-main"><span class="title-kicker">PRESENTATION</span>Title Goes Here!</h1>
  <p class="title-sub">Subtitle of Presentation Goes Here</p>
  <p class="title-date">September 20, 2024</p>
  <footer class="foot">Copyright © 2024 Crewvantor. All rights reserved.</footer>
</section>

<!-- Title dark, city photo -->
<section class="slide title-slide dark" style="left:610px;top:784px">
  <p class="site-url">www.crewvantor.com/</p>
  <div class="photo-city title-photo" role="img" aria-label="Photo of office towers in a city"></div>
  <div class="title-overlay"></div>
  <div class="brand title-brand"><span class="brand-mark"></span>CREWVANTOR</div>
  <h1 class="title-main"><span class="title-kicker">PRESENTATION</span>Title Goes Here!</h1>
  <p class="title-sub">Subtitle of Presentation Goes Here</p>
  <p class="title-date">September 20, 2024</p>
  <footer class="foot">Copyright © 2024 Crewvantor. All rights reserved.</footer>
</section>

<!-- Title light, meeting photo -->
<section class="slide title-slide" style="left:30px;top:1120px">
  <p class="site-url">www.crewvantor.com/</p>
  <div class="photo title-photo" role="img" aria-label="Photo of colleagues in a meeting"></div>
  <div class="title-overlay"></div>
  <div class="brand title-brand"><span class="brand-mark"></span>CREWVANTOR</div>
  <h1 class="title-main"><span class="title-kicker">PRESENTATION</span>Title Goes Here!</h1>
  <p class="title-sub">Subtitle of Presentation Goes Here</p>
  <p class="title-date">September 20, 2024</p>
  <footer class="foot">Copyright © 2024 Crewvantor. All rights reserved.</footer>
</section>

<!-- Title dark, aerial city photo -->
<section class="slide title-slide dark" style="left:610px;top:1120px">
  <p class="site-url">www.crewvantor.com/</p>
  <div class="photo-city title-photo" role="img" aria-label="Aerial photo of a city"></div>
  <div class="title-overlay"></div>
  <div class="brand title-brand"><span class="brand-mark"></span>CREWVANTOR</div>
  <h1 class="title-main"><span class="title-kicker">PRESENTATION</span>Title Goes Here!</h1>
  <p class="title-sub">Subtitle of Presentation Goes Here</p>
  <p class="title-date">September 20, 2024</p>
  <footer class="foot">Copyright © 2024 Crewvantor. All rights reserved.</footer>
</section>

<!-- Table of contents -->
<section class="slide toc-slide" style="left:30px;top:1456px">
  <div class="title-mark" style="top:16px"></div>
  <h2 class="slide-title" style="top:30px">Table of Contents</h2>
  <ul class="toc-list">
    <li class="toc-item"><span class="toc-num">1</span><div><p class="toc-head">Title Goes Here</p><p class="body-copy">Short summary of this section goes right here.</p></div></li>
    <li class="toc-item"><span class="toc-num">4</span><div><p class="toc-head">Title Goes Here</p><p class="body-copy">Short summary of this section goes right here.</p></div></li>
    <li class="toc-item"><span class="toc-num">2</span><div><p class="toc-head">Title Goes Here</p><p class="body-copy">Short summary of this section goes right here.</p></div></li>
    <li class="toc-item"><span class="toc-num">5</span><div><p class="toc-head">Title Goes Here</p><p class="body-copy">Short summary of this section goes right here.</p></div></li>
    <li class="toc-item"><span class="toc-num">3</span><div><p class="toc-head">Title Goes Here</p><p class="body-copy">Short summary of this section goes right here.</p></div></li>
    <li class="toc-item"><span class="toc-num">6</span><div><p class="toc-head">Title Goes Here</p><p class="body-copy">Short summary of this section goes right here.</p></div></li>
  </ul>
  <footer class="foot">Copyright © 2024 Crewvantor</footer>
</section>

<!-- About us -->
<section class="slide about-slide" style="left:610px;top:1456px">
  <h2 class="about-title">About Us</h2>
  <div class="about-rule"></div>
  <p class="body-copy about-copy">Crewvantor is dedicated to delivering reliable service to businesses of every size. Our team brings years of practical experience, careful planning and honest communication to each project. We listen closely, plan with care and work alongside our clients to reach clear, lasting results that support steady growth.</p>
  <div class="about-frame"></div>
  <div class="photo about-photo" role="img" aria-label="Photo of a team working together at a table"></div>
  <footer class="foot">Copyright © 2024 Crewvantor</footer>
</section>

<!-- Two photos -->
<section class="slide duo-slide" style="left:30px;top:1792px">
  <div class="photo duo-photo" style="left:40px" role="img" aria-label="Photo of colleagues talking"></div>
  <div class="photo duo-photo" style="left:300px" role="img" aria-label="Photo of a group of coworkers"></div>
  <h3 class="duo-head" style="left:40px">Title Goes Here!</h3>
  <h3 class="duo-head" style="left:300px">Title Goes Here!</h3>
  <p class="body-copy duo-copy" style="left:40px">Add a short paragraph here that explains the topic of this slide. Keep the wording brief, clear and easy to read for every audience.</p>
  <p class="body-copy duo-copy" style="left:300px">Add a short paragraph here that explains the topic of this slide. Keep the wording brief, clear and easy to read for every audience.</p>
  <footer class="foot">Copyright © 2024 Crewvantor</footer>
</section>

<!-- Meet the team -->
<section class="slide team-slide" style="left:610px;top:1792px">
  <div class="photo-city team-band" role="img" aria-label="Photo of office buildings"></div>
  <div class="team-band-tint"></div>
  <h2 class="team-title">Meet The Team</h2>
  <div class="member" style="left:40px"><div class="member-photo" role="img" aria-label="Portrait of team member"></div><p class="member-name">DANA ELLISON</p><p class="member-role">Title</p><p class="body-copy">Short bio for this team member goes here.</p></div>
  <div class="member" style="left:210px"><div class="member-photo" role="img" aria-label="Portrait of team member"></div><p class="member-name">MARA QUINTON</p><p class="member-role">Title</p><p class="body-copy">Short bio for this team member goes here.</p></div>
  <div class="member" style="left:380px"><div class="member-photo" role="img" aria-label="Portrait of team member"></div><p class="member-name">OWEN TALBOT</p><p class="member-role">Title</p><p class="body-copy">Short bio for this team member goes here.</p></div>
  <footer class="foot">Copyright © 2024 Crewvantor</footer>
</section>

<!-- Core values -->
<section class="slide values-slide" style="left:30px;top:2128px">
  <div class="photo values-band" role="img" aria-label="Photo of a modern office"></div>
  <div class="values-tint"></div>
  <h2 class="values-title">Our Core Values</h2>
  <p class="body-copy values-intro">A short statement about the values that guide our work, our people and the way we serve every client.</p>
  <div class="values-row">
    <div><div class="value-icon"></div><p class="value-name">INTEGRITY</p><p class="body-copy">We act honestly and keep our word.</p></div>
    <div><div class="value-icon"></div><p class="value-name">FAMILY</p><p class="body-copy">We care for our team and clients.</p></div>
    <div><div class="value-icon"></div><p class="value-name">RESPECT</p><p class="body-copy">We value every voice and idea.</p></div>
    <div><div class="value-icon"></div><p class="value-name">PASSION</p><p class="body-copy">We bring energy to every task.</p></div>
  </div>
  <footer class="foot">Copyright © 2024 Crewvantor</footer>
</section>

<!-- Pyramid -->
<section class="slide pyramid-slide" style="left:610px;top:2128px">
  <div class="title-mark" style="top:16px"></div>
  <h2 class="slide-title" style="top:30px">Slide Title Goes Here!</h2>
  <svg class="pyr-svg" width="220" height="170" viewBox="0 0 220 170" aria-hidden="true">
    <polygon points="110,0 145,55 75,55" fill="#1f9c98"/>
    <polygon points="72,60 148,60 182,113 38,113" fill="#4db3af"/>
    <polygon points="35,118 185,118 218,170 2,170" fill="#8fd0cc"/>
  </svg>
  <div class="pyr-note" style="left:40px;top:110px"><h3>Title Goes Here</h3><p class="body-copy">Brief note about this level.</p></div>
  <div class="pyr-note" style="left:420px;top:80px"><h3>Title Goes Here</h3><p class="body-copy">Brief note about this level.</p></div>
  <div class="pyr-note" style="left:420px;top:210px"><h3>Title Goes Here</h3><p class="body-copy">Brief note about this level.</p></div>
  <footer class="foot">Copyright © 2024 Crewvantor</footer>
</section>

<!-- Process -->
<section class="slide process-slide" style="left:30px;top:2464px">
  <h2 class="slide-title" style="top:30px">Our Process</h2>
  <div class="process-line"></div>
  <div class="step" style="left:30px"><div class="step-num">1</div><p class="step-head">Title Goes Here</p><p class="body-copy">Describe this step in a few short words.</p></div>
  <div class="step" style="left:160px"><div class="step-num">2</div><p class="step-head">Title Goes Here</p><p class="body-copy">Describe this step in a few short words.</p></div>
  <div class="step" style="left:290px"><div class="step-num">3</div><p class="step-head">Title Goes Here</p><p class="body-copy">Describe this step in a few short words.</p></div>
  <div class="step" style="left:420px"><div class="step-num">4</div><p class="step-head">Title Goes Here</p><p class="body-copy">Describe this step in a few short words.</p></div>
  <footer class="foot">Copyright © 2024 Crewvantor</footer>
</section>

<!-- Table -->
<section class="slide table-slide" style="left:610px;top:2464px">
  <div class="title-mark" style="top:16px"></div>
  <h2 class="slide-title" style="top:30px">Table Slide</h2>
  <table class="data-table">
    <tr><th>Heading</th><th>Title 1</th><th>Title 2</th><th>Title 3</th><th>Title 4</th><th>Title 5</th></tr>
    <tr><td>Row label goes here</td><td>10</td><td>24</td><td>18</td><td>32</td><td>15</td></tr>
    <tr><td>Row label goes here</td><td>12</td><td>20</td><td>26</td><td>14</td><td>30</td></tr>
    <tr><td>Row label goes here</td><td>16</td><td>28</td><td>22</td><td>19</td><td>11</td></tr>
    <tr><td>Row label goes here</td><td>21</td><td>13</td><td>17</td><td>25</td><td>29</td></tr>
    <tr><td>Row label goes here</td><td>18</td><td>30</td><td>12</td><td>23</td><td>20</td></tr>
    <tr><td>Row label goes here</td><td>27</td><td>15</td><td>24</td><td>16</td><td>22</td></tr>
  </table>
  <footer class="foot">Copyright © 2024 Crewvantor</footer>
</section>

<!-- Chart -->
<section class="slide chart-slide" style="left:30px;top:2800px">
  <h2 class="slide-title" style="top:26px">Chart Slide</h2>
  <svg class="chart-svg" width="290" height="220" viewBox="0 0 290 220" aria-hidden="true">
    <g stroke="#d9e0e3" stroke-width="1">
      <line x1="20" y1="20" x2="285" y2="20"/><line x1="20" y1="70" x2="285" y2="70"/>
      <line x1="20" y1="120" x2="285" y2="120"/><line x1="20" y1="170" x2="285" y2="170"/>
    </g>
    <line x1="20" y1="200" x2="285" y2="200" stroke="#8a949c"/>
    <g fill="#1f9c98">
      <rect x="32" y="110" width="12" height="90"/><rect x="92" y="70" width="12" height="130"/>
      <rect x="152" y="130" width="12" height="70"/><rect x="212" y="40" width="12" height="160"/>
    </g>
    <g fill="#8fd0cc">
      <rect x="46" y="140" width="12" height="60"/><rect x="106" y="100" width="12" height="100"/>
      <rect x="166" y="90" width="12" height="110"/><rect x="226" y="80" width="12" height="120"/>
    </g>
    <g fill="#1c2833">
      <rect x="60" y="160" width="12" height="40"/><rect x="120" y="120" width="12" height="80"/>
      <rect x="180" y="150" width="12" height="50"/><rect x="240" y="110" width="12" height="90"/>
    </g>
    <g fill="#8a949c" font-size="7" font-family="Arimo, Arial, sans-serif" text-anchor="middle">
      <text x="52" y="211">Item 1</text><text x="112" y="211">Item 2</text>
      <text x="172" y="211">Item 3</text><text x="232" y="211">Item 4</text>
    </g>
  </svg>
  <table class="chart-table">
    <tr><th>Category</th><th>Series 1</th><th>Series 2</th><th>Series 3</th></tr>
    <tr><td>Item 1</td><td>4.3</td><td>2.4</td><td>2.0</td></tr>
    <tr><td>Item 2</td><td>6.5</td><td>5.0</td><td>4.0</td></tr>
    <tr><td>Item 3</td><td>3.5</td><td>5.5</td><td>2.5</td></tr>
    <tr><td>Item 4</td><td>8.0</td><td>6.0</td><td>4.5</td></tr>
  </table>
  <footer class="foot">Copyright © 2024 Crewvantor</footer>
</section>

<!-- Contact -->
<section class="slide contact-slide dark" style="left:610px;top:2800px">
  <div class="photo-city contact-bg" role="img" aria-label="Aerial photo of city buildings"></div>
  <div class="contact-tint"></div>
  <div class="brand contact-brand"><span class="brand-mark"></span>CREWVANTOR</div>
  <h2 class="contact-head">Contact Us</h2>
  <ul class="contact-list">
    <li><span class="contact-icon"><svg width="8" height="8" viewBox="0 0 24 24" aria-hidden="true"><path fill="#fff" d="M6.6 10.8a15 15 0 0 0 6.6 6.6l2.2-2.2a1 1 0 0 1 1-.25 11.4 11.4 0 0 0 3.6.57 1 1 0 0 1 1 1V20a1 1 0 0 1-1 1A17 17 0 0 1 3 4a1 1 0 0 1 1-1h3.5a1 1 0 0 1 1 1c0 1.25.2 2.45.57 3.6a1 1 0 0 1-.25 1z"/></svg></span>(555) 014-2290</li>
    <li><span class="contact-icon"><svg width="8" height="8" viewBox="0 0 24 24" aria-hidden="true"><path fill="#fff" d="M2 5h20v14H2z"/><path d="M2 5l10 8 10-8" stroke="#1f9c98" stroke-width="2" fill="none"/></svg></span>hello@crewvantor.com</li>
    <li><span class="contact-icon"><svg width="8" height="8" viewBox="0 0 24 24" aria-hidden="true"><circle cx="12" cy="12" r="9" stroke="#fff" stroke-width="2.5" fill="none"/><path d="M3 12h18M12 3c3 3 3 15 0 18M12 3c-3 3-3 15 0 18" stroke="#fff" stroke-width="2" fill="none"/></svg></span>www.crewvantor.com/</li>
  </ul>
  <footer class="foot">Copyright © 2024 Crewvantor</footer>
</section>

</body>
</html>
```